Web Design Project - Event Management Company

A web-page design needs to be created for an event management company. The logo has already been created, the design needs to draw on the themes and colors of the logo and extend on that.

The event management company likes to differentiate itself from others by being a bit "un-conventional" and being able to think outside the box.

the specialise in corporate events, weddings, AGMs, anything that requires coordination of resources. They also can provide Audio Visual services such as recording events.

final design will also require HTML implementation

```html
<!DOCTYPE html>
<html lang="en">
<head>
<meta charset="utf-8">
<title>Odd Block Events</title>
<link rel="stylesheet" href="https://fonts.googleapis.com/css2?family=Jost:wght@300;400;500;700&display=swap">
<style>
:root{
  --white:#ffffff;
  --orange:#e75e24;
  --sky:#68c4e2;
  --sky-deep:#4fb6da;
  --lime:#cfd016;
  --pink:#f4c6d3;
  --form-bg:#efefef;
  --form-line:#c9c9c9;
  --ink:#555555;
}
*{box-sizing:border-box;margin:0;padding:0}
html,body{width:1200px;height:3721px;overflow:hidden}
body{position:relative;background:var(--white);font-family:"Jost",sans-serif;color:var(--white)}
.band{position:absolute;left:0;width:1200px}
.hero{top:403px;height:502px;background:var(--orange)}
.services{top:946px;height:899px;background:var(--orange)}
.events{top:1882px;height:899px;background:var(--sky)}
.contact{top:2821px;height:900px;background:var(--lime)}

.brand-mark{position:absolute;top:218px;left:478px;width:244px;height:244px;background:var(--sky)}
.brand-name{position:absolute;top:104px;left:0;width:1200px;text-align:center;font-weight:400;font-size:68px;line-height:86px;letter-spacing:1px;text-transform:uppercase}
.tagline{position:absolute;top:213px;left:423px;width:359px;height:52px;border:4px solid var(--white);text-align:center;font-weight:500;font-size:26px;line-height:44px;letter-spacing:1px;text-transform:uppercase}

.chevron{position:absolute;left:554px;width:92px;height:52px}

.section-title{position:absolute;top:40px;left:0;width:1200px;text-align:center;font-weight:700;font-size:56px;letter-spacing:3px;text-transform:uppercase}

.service{position:absolute;top:197px;width:300px}
.service-badge{width:248px;height:248px;border-radius:50%;background:var(--white);display:flex;align-items:center;justify-content:center}
.service-icon{width:140px;height:150px;border-radius:30px}
.icon-watch{background:var(--lime)}
.icon-gem{background:var(--pink)}
.icon-thumb{background:var(--sky)}
.service-name{margin-top:34px;font-weight:300;font-size:58px;line-height:1}
.service-text{margin-top:14px;width:262px;font-size:18px;line-height:1.16}

.event-card{position:absolute;width:309px;height:306px;background:var(--white);padding:6px}
.event-title{height:46px;font-weight:700;font-size:27px;line-height:46px;color:var(--sky-deep);text-transform:uppercase;padding-left:4px}
.event-photo{width:297px;height:248px}
.photo-spoons{background:linear-gradient(135deg,#c9b8a4,#7a5e48)}
.photo-toast{background:linear-gradient(135deg,#e8d6c6,#8a6d57)}
.photo-dinner{background:linear-gradient(135deg,#6b4a2f,#1d1b1a)}
.photo-hall{background:linear-gradient(135deg,#8a6a42,#241a12)}
.photo-flowers{background:linear-gradient(135deg,#efe8df,#c7a8a3)}

.contact-lead{position:absolute;top:118px;left:0;width:1200px;text-align:center;font-weight:400;font-size:38px;letter-spacing:1px}

.contact-form{position:absolute;top:229px;left:396px;width:401px;height:414px;background:var(--form-bg);border-radius:10px;color:var(--ink);padding:14px 20px}
.form-title{font-size:24px;font-weight:400;text-transform:uppercase}
.form-sub{font-size:10px;text-transform:uppercase;margin-top:2px;color:#888}
.form-row{position:absolute;left:21px;display:flex;align-items:flex-start}
.form-label{width:148px;font-size:10px;text-transform:uppercase;padding-top:7px}
.form-field{width:127px;height:25px;background:var(--white);border:1px solid var(--form-line)}
.form-select{width:82px;font-size:11px;line-height:23px;padding-left:5px;position:relative}
.form-select::after{content:"";position:absolute;right:6px;top:9px;border:4px solid transparent;border-top-color:var(--ink)}
.form-area{width:120px;height:87px}
.form-button{position:absolute;top:365px;height:26px;padding:0 10px;background:var(--white);border:1px solid var(--form-line);border-radius:3px;font-size:12px;line-height:24px}

.call-label{position:absolute;top:650px;left:0;width:1200px;text-align:center;font-size:17px;font-weight:500;text-transform:uppercase}
.phone{position:absolute;top:668px;left:0;width:1200px;text-align:center;font-size:42px;font-weight:500;letter-spacing:1px}
.social{position:absolute;top:739px;left:560px;display:flex;gap:4px}
.social-square{width:36px;height:36px;border-radius:4px;background:var(--sky-deep)}
.social-square:first-child{background:#3b5a9a}
</style>
</head>
<body>

<div class="brand-mark"></div>

<header class="band hero">
  <h1 class="brand-name">Odd Block Events</h1>
  <div class="tagline">Let us entertain you</div>
  <svg class="chevron" style="top:418px" viewBox="0 0 92 52"><polyline points="8,8 46,44 84,8" fill="none" stroke="#fff" stroke-width="13" stroke-linecap="round" stroke-linejoin="round"/></svg>
</header>

<section class="band services">
  <h2 class="section-title">What we do</h2>
  <div class="service" style="left:71px">
    <div class="service-badge" style="margin-left:3px"><div class="service-icon icon-watch" role="img" aria-label="Wristwatch icon"></div></div>
    <h3 class="service-name">Corporate</h3>
    <p class="service-text">This is where you put a couple great sentences about this specific service and what it entails. Any of this information can be changed as often as you want, fully customizable</p>
  </div>
  <div class="service" style="left:504px">
    <div class="service-badge" style="margin-left:-19px"><div class="service-icon icon-gem" role="img" aria-label="Diamond icon"></div></div>
    <h3 class="service-name">Social</h3>
    <p class="service-text">This is where you put a couple great sentences about this specific service and what it entails. Any of this information can be changed as often as you want, fully customizable</p>
  </div>
  <div class="service" style="left:865px">
    <div class="service-badge" style="margin-left:9px"><div class="service-icon icon-thumb" role="img" aria-label="Thumbs up icon"></div></div>
    <h3 class="service-name">Business</h3>
    <p class="service-text">This is where you put a couple great sentences about this specific service and what it entails. Any of this information can be changed as often as you want, fully customizable</p>
  </div>
  <svg class="chevron" style="top:812px" viewBox="0 0 92 52"><polyline points="8,8 46,44 84,8" fill="none" stroke="#fff" stroke-width="13" stroke-linecap="round" stroke-linejoin="round"/></svg>
</section>

<section class="band events">
  <h2 class="section-title">Recent events</h2>
  <article class="event-card" style="left:114px;top:136px">
    <h3 class="event-title">Event title</h3>
    <div class="event-photo photo-spoons" role="img" aria-label="Photo of silver spoons on a table"></div>
  </article>
  <article class="event-card" style="left:448px;top:136px">
    <h3 class="event-title">Event title</h3>
    <div class="event-photo photo-toast" role="img" aria-label="Photo of guests raising a toast"></div>
  </article>
  <article class="event-card" style="left:782px;top:136px">
    <h3 class="event-title">Event title</h3>
    <div class="event-photo photo-dinner" role="img" aria-label="Photo of a set banquet table"></div>
  </article>
  <article class="event-card" style="left:114px;top:463px">
    <h3 class="event-title">Event title</h3>
    <div class="event-photo photo-hall" role="img" aria-label="Photo of a conference hall with a screen"></div>
  </article>
  <article class="event-card" style="left:448px;top:463px">
    <h3 class="event-title">Event title</h3>
    <div class="event-photo photo-flowers" role="img" aria-label="Photo of a wedding table bouquet"></div>
  </article>
  <svg class="chevron" style="top:812px" viewBox="0 0 92 52"><polyline points="8,8 46,44 84,8" fill="none" stroke="#fff" stroke-width="13" stroke-linecap="round" stroke-linejoin="round"/></svg>
</section>

<section class="band contact">
  <h2 class="section-title">Work with us</h2>
  <p class="contact-lead">Fill out our event form and we will be in touch soon!</p>
  <div class="contact-form">
    <div class="form-title">Fancy contact form</div>
    <div class="form-sub">Drop us a line and we will get back to you</div>
    <div class="form-row" style="top:92px"><span class="form-label">Name</span><span class="form-field"></span></div>
    <div class="form-row" style="top:140px"><span class="form-label">Email</span><span class="form-field"></span></div>
    <div class="form-row" style="top:185px"><span class="form-label">Subject</span><span class="form-field form-select">--Choose--</span></div>
    <div class="form-row" style="top:222px"><span class="form-label">Message</span><span class="form-field form-area"></span></div>
    <div class="form-row" style="top:327px"><span class="form-label">3 + 3 =</span><span class="form-field"></span></div>
    <span class="form-button" style="left:86px">Submit</span>
    <span class="form-button" style="left:164px">Reset</span>
  </div>
  <div class="call-label">Call us today!</div>
  <div class="phone">000-000-000</div>
  <div class="social"><span class="social-square"></span><span class="social-square"></span></div>
</section>

</body>
</html>
```